Website design for commercial and residential security company

we're looking to see some new designs for an established company with no website.

homepage and one inner page

here is a link to the homepage content, sitemap, logo and more.
https://files.brontavel.net/share/7QxmPzLrTw2vNkdJhYcsa9eFgbUoiVwRn?view=open

call to action should be Request A Quote

if you have any questions please send them to us asap

thank you

1 page

Sans Serif

```html
<!DOCTYPE html>
<html lang="en">
<head>
<meta charset="utf-8">
<title>Polar Gate Security – Residential &amp; Commercial Security Solutions</title>
<link href="https://fonts.googleapis.com/css2?family=Poppins:wght@300;400;500;600;700&family=Roboto:wght@400;500;700&display=swap" rel="stylesheet">
<style>
:root{
  --gold:#d2a22a;
  --gold-dark:#b98c1c;
  --ink:#222;
  --text:#555;
  --muted:#888;
  --light:#f4f4f4;
  --dark:#2e2e2e;
  --darker:#242424;
  --white:#fff;
}
*{box-sizing:border-box;margin:0;padding:0}
html,body{width:1200px;height:5040px;overflow:hidden}
body{font-family:'Poppins',sans-serif;color:var(--text);background:var(--white);position:relative}
section,header,footer{position:absolute;left:0;width:1200px}
.abs{position:absolute}
.photo{position:absolute}
.btn{display:inline-block;font-size:11px;font-weight:600;text-transform:uppercase;letter-spacing:.5px;border-radius:20px;padding:11px 26px;text-decoration:none}
.btn-gold{background:var(--gold);color:var(--white)}
.btn-white{background:var(--white);color:var(--ink)}
.eyebrow{font-size:10px;font-weight:600;letter-spacing:2px;text-transform:uppercase;color:var(--gold);display:flex;align-items:center;justify-content:center;gap:10px}
.eyebrow::before,.eyebrow::after{content:"";width:34px;height:2px;background:var(--gold)}
.section-title{font-family:'Roboto',sans-serif;font-weight:500;color:var(--ink);font-size:30px;text-align:center}

/* header */
.site-header{top:0;height:80px;z-index:5}
.logo{position:absolute;left:150px;top:14px;display:flex;align-items:center;gap:10px;color:var(--gold);font-weight:700;font-size:22px;letter-spacing:1px;text-transform:uppercase}
.logo .mark{width:16px;height:16px;background:var(--gold)}
.nav{position:absolute;left:460px;top:26px;display:flex;gap:34px;font-size:12px;font-weight:500;color:var(--ink);text-transform:uppercase}
.nav .active{color:var(--gold)}
.site-header .btn{position:absolute;left:914px;top:14px;border-radius:3px;padding:11px 18px}

/* hero */
.hero{top:0;height:800px}
.hero .photo{inset:0 0 40px 0;background:linear-gradient(100deg,#3b3a36 0%,#7a756c 35%,#cfc8bb 65%,#e8e3da 100%)}
.hero-text{position:absolute;left:150px;top:262px;color:var(--white)}
.hero-text p{font-size:21px;font-weight:300}
.hero-text h1{font-size:40px;font-weight:500;line-height:1.15;margin-top:14px}
.hero-text h1 .amp{color:var(--gold)}
.hero-text h1 strong{font-weight:700;font-size:46px}
.hero-btns{position:absolute;left:150px;top:466px;display:flex;gap:16px}
.hero svg{position:absolute;left:0;bottom:0}

/* feature rows */
.feature{height:520px}
.feature h2{font-size:26px;font-weight:700;color:var(--ink)}
.feature .lead{font-size:15px;line-height:1.55;color:#444;margin-top:18px}
.feature .body{font-size:11px;line-height:1.7;color:var(--muted);margin-top:14px}
.feature .btn{margin-top:24px}
.card{position:absolute;background:var(--white);box-shadow:0 6px 24px rgba(0,0,0,.15)}
.card .photo{inset:20px}
.gold-bar{position:absolute;background:var(--gold)}

/* commercial band */
.commercial{top:2088px;height:392px;text-align:center;color:var(--white)}
.commercial .photo{inset:0;background:linear-gradient(180deg,#243449 0%,#1d2838 55%,#2e3c52 100%)}
.commercial .inner{position:relative;padding-top:60px}
.commercial .eyebrow{color:#d8d8d8}
.commercial .eyebrow::before,.commercial .eyebrow::after{background:#d8d8d8}
.commercial h2{font-size:27px;font-weight:600;margin-top:10px}
.commercial .lead{font-size:14px;line-height:1.5;margin:10px auto 0;width:520px}
.commercial .body{font-size:11px;line-height:1.6;margin:18px auto 0;width:520px;color:#cfd4dc}
.commercial .btn{margin-top:30px}

/* industries */
.industries{top:2580px;height:520px}
.industries .photo{left:0;top:0;width:368px;height:520px;border-radius:0 40px 40px 0;background:linear-gradient(150deg,#4a4f58 0%,#2a2d33 50%,#8c6a3e 100%)}
.industries h2{position:absolute;left:460px;top:20px;font-size:46px;font-weight:600;color:var(--gold)}
.industries h2 span{font-weight:400;color:var(--ink)}
.ind-col{position:absolute;top:140px;width:300px}
.ind-col svg{display:block;margin-left:4px}
.ind-col h3{font-size:21px;font-weight:400;color:var(--ink);margin-top:22px}
.ind-col h3 span{color:var(--gold);font-weight:600}
.ind-col ul{list-style:none;margin-top:22px}
.ind-col li{font-size:13px;color:#555;line-height:1.45;margin-bottom:15px}
.ind-col a{font-size:12px;font-weight:600;color:var(--gold);text-decoration:none}

/* testimonials */
.testimonials{top:3220px;height:400px;background:var(--light)}
.testimonials .head{position:absolute;top:22px;width:100%}
.testimonials .section-title{margin-top:10px}
.slider-line{position:absolute;left:190px;top:108px;width:820px;height:1px;background:#bbb}
.arrow{position:absolute;top:102px}
.t-card{position:absolute;top:132px;width:320px;height:242px;background:var(--white);box-shadow:0 2px 10px rgba(0,0,0,.06);padding:26px 26px}
.t-card .name{font-size:13px;font-weight:600;color:var(--ink);text-transform:uppercase}
.t-card .role{font-size:10px;color:var(--muted);margin-top:2px}
.stars{color:var(--gold);font-size:20px;letter-spacing:3px;margin-top:12px}
.quote{font-family:Georgia,serif;font-size:48px;color:var(--gold);line-height:.6;margin-top:18px;height:24px}
.t-card p{font-size:10px;line-height:1.7;color:var(--muted);margin-top:8px}

/* cta band */
.cta{top:3660px;height:384px;text-align:center;color:var(--white)}
.cta .photo{inset:0;background:linear-gradient(90deg,#2a2620 0%,#6b5a45 45%,#9a8a76 70%,#4b433a 100%)}
.cta .inner{position:relative;padding-top:84px}
.cta .eyebrow{color:#eee}
.cta .eyebrow::before,.cta .eyebrow::after{background:#eee}
.cta h2{font-size:30px;font-weight:600;line-height:1.25;margin-top:12px}
.cta .btn{margin-top:28px}

/* news */
.news{top:4100px;height:600px}
.news .head{position:absolute;top:28px;width:100%}
.news .section-title{margin-top:8px}
.news-main{position:absolute;left:240px;top:116px;width:360px;height:460px;background:var(--white);box-shadow:0 4px 18px rgba(0,0,0,.1)}
.news-main .photo{left:0;top:0;width:360px;height:280px;background:linear-gradient(160deg,#6f8fb3 0%,#c7d3e1 50%,#5b5f66 100%)}
.news-main .content{position:absolute;left:26px;top:300px;right:26px}
.news h3{font-size:13px;font-weight:600;color:var(--ink);text-transform:uppercase;line-height:1.35}
.news .date{font-size:9px;color:var(--muted);margin-top:4px}
.news-main p{font-size:10px;line-height:1.7;color:var(--muted);margin-top:8px}
.news-item{position:absolute;left:600px;width:360px;height:140px;background:var(--white);box-shadow:0 4px 18px rgba(0,0,0,.08);display:flex;align-items:center;gap:20px;padding:0 18px}
.news-item .thumb{width:110px;height:110px;flex:none}
.news-item .meta{width:190px}

/* footer */
.site-footer{top:4720px;height:320px;background:var(--dark);color:#ccc}
.site-footer .logo{left:180px;top:40px;font-size:20px}
.f-col{position:absolute;top:100px}
.f-col h4{font-size:13px;font-weight:600;color:var(--white);text-transform:uppercase;margin-bottom:14px}
.f-col p,.f-col li{font-size:11px;line-height:1.7;color:#bbb}
.f-col ul{list-style:none}
.contact-line{display:flex;gap:10px;align-items:flex-start;margin-bottom:10px}
.newsletter{display:flex;margin-top:16px}
.newsletter .field{width:210px;height:36px;border:1px solid #777;border-radius:18px 0 0 18px;font-size:10px;color:#999;padding:11px 16px}
.newsletter .go{height:36px;background:var(--gold);color:var(--white);font-size:10px;font-weight:600;padding:11px 16px;border-radius:0 18px 18px 0}
.f-bottom{position:absolute;left:0;top:250px;width:1200px;height:70px;background:var(--darker);border-top:1px solid #444}
.socials{position:absolute;left:190px;top:22px;display:flex;gap:10px}
.socials span{width:26px;height:26px;border-radius:50%;background:var(--gold)}
.copy{position:absolute;right:190px;top:27px;font-size:10px;color:#999}
</style>
</head>
<body>

<header class="site-header">
  <div class="logo"><span class="mark"></span>Polar Gate</div>
  <nav class="nav">
    <span class="active">Home</span><span>About</span><span>Solutions ▾</span><span>Resources</span><span>Contact</span>
  </nav>
  <a class="btn btn-gold">Request a Quote</a>
</header>

<section class="hero">
  <div class="photo" role="img" aria-label="Woman relaxing on a sofa in a bright living room"></div>
  <div class="hero-text">
    <p>We provide a wide range of</p>
    <h1>Residential <span class="amp">&amp;</span> Commercial<br><strong>Security Solutions</strong></h1>
  </div>
  <div class="hero-btns">
    <a class="btn btn-gold">Get a Free Quote</a>
    <a class="btn btn-white">Learn More</a>
  </div>
  <svg width="1200" height="140" viewBox="0 0 1200 140">
    <path d="M0 50 C300 140 900 140 1200 30 L1200 140 L0 140 Z" fill="#fff"/>
    <path d="M0 70 C300 150 900 150 1200 50" fill="none" stroke="#d2a22a" stroke-width="3"/>
    <rect x="588" y="58" width="24" height="36" rx="12" fill="none" stroke="#999" stroke-width="2"/>
    <line x1="600" y1="66" x2="600" y2="74" stroke="#999" stroke-width="2"/>
  </svg>
</section>

<section class="feature" style="top:880px">
  <div class="abs" style="left:192px;top:46px;width:330px">
    <h2>Residential Security</h2>
    <p class="lead">Consider a home surveillance device that would do more for you and your family than you ever imagined.</p>
    <p class="body">Our licensed team brings trusted monitoring to your door, and each installation is handled with care by skilled local staff.</p>
    <a class="btn btn-gold">Learn More</a>
  </div>
  <div class="gold-bar" style="left:760px;top:290px;width:370px;height:110px"></div>
  <div class="photo" style="left:600px;top:56px;width:520px;height:340px;background:linear-gradient(120deg,#d9d6d0 0%,#a89b8a 50%,#5d4c3d 100%)" role="img" aria-label="Woman entering a code on a wall alarm keypad"></div>
  <div class="card" style="left:368px;top:292px;width:344px;height:228px">
    <div class="photo" style="background:linear-gradient(180deg,#efefef,#cfcfcf)" role="img" aria-label="White alarm control panel with keypad"></div>
  </div>
</section>

<section class="feature" style="top:1500px">
  <div class="gold-bar" style="left:180px;top:40px;width:14px;height:330px"></div>
  <div class="photo" style="left:194px;top:14px;width:406px;height:368px;background:linear-gradient(140deg,#4b3826 0%,#9c8468 50%,#d7ccbd 100%)" role="img" aria-label="Security camera mounted on a brick wall"></div>
  <div class="card" style="left:500px;top:280px;width:224px;height:208px">
    <div class="photo" style="background:linear-gradient(180deg,#f2f2f2,#d5d5d5)" role="img" aria-label="Black bullet surveillance camera"></div>
  </div>
  <div class="abs" style="left:730px;top:22px;width:300px">
    <h2>Residential Security</h2>
    <p class="lead">Consider a home surveillance device that would do more for you and your family than you ever imagined.</p>
    <p class="body">Our licensed team brings trusted monitoring to your door, and each installation is handled with care by skilled local staff.</p>
    <a class="btn btn-gold">Learn More</a>
  </div>
</section>

<section class="commercial">
  <div class="photo" role="img" aria-label="Business team meeting around a table in an office"></div>
  <div class="inner">
    <div class="eyebrow">Security</div>
    <h2>Commercial Security</h2>
    <p class="lead">Protect assets and security of your business with exceptional Commercial Security installation.</p>
    <p class="body">Whether a store or a large facility, we design layered systems that keep your people, stock and premises safe every hour of the day.</p>
    <a class="btn btn-gold">Learn More</a>
  </div>
</section>

<section class="industries">
  <div class="photo" role="img" aria-label="Woman watching monitors in a security control room"></div>
  <h2>Industries <span>we serve</span></h2>
  <div class="ind-col" style="left:466px">
    <svg width="46" height="42" viewBox="0 0 46 42" fill="none" stroke="#777" stroke-width="2"><rect x="4" y="10" width="38" height="30"/><path d="M1 10 H45 M10 18h6v6h-6z M20 18h6v6h-6z M30 18h6v6h-6z M18 40V30h10v10"/><path d="M8 10V3h30v7"/></svg>
    <h3>Commercial <span>Security</span></h3>
    <ul>
      <li>Audio &amp; Video Solutions</li>
      <li>Burglar Alarms &amp; Detection</li>
      <li>CCTV cameras</li>
      <li>Monitoring of alarms</li>
      <li>Alarm systems and cameras<br>properly installed</li>
    </ul>
    <a>Learn More</a>
  </div>
  <div class="ind-col" style="left:796px">
    <svg width="46" height="42" viewBox="0 0 46 42" fill="none" stroke="#777" stroke-width="2"><path d="M4 40V12L23 2l19 10v28z"/><path d="M12 18h8v8h-8z M26 18h8v8h-8z M12 30h8v10h-8z M26 30h8v8h-8z"/></svg>
    <h3>Residential <span>Security</span></h3>
    <ul>
      <li>Residential Alarm</li>
      <li>Residential Network Wi-Fi</li>
      <li>CCTV and Residential</li>
      <li>Home Automation</li>
    </ul>
    <a>Learn More</a>
  </div>
</section>

<section class="testimonials">
  <div class="head">
    <div class="eyebrow">Testimonial</div>
    <h2 class="section-title">What Our Clients Have To Say</h2>
  </div>
  <div class="slider-line"></div>
  <svg class="arrow" style="left:186px" width="14" height="12" viewBox="0 0 14 12"><path d="M13 6H2M6 1L1 6l5 5" fill="none" stroke="#555" stroke-width="1.5"/></svg>
  <svg class="arrow" style="left:1000px" width="14" height="12" viewBox="0 0 14 12"><path d="M1 6h11M8 1l5 5-5 5" fill="none" stroke="#555" stroke-width="1.5"/></svg>
  <div class="t-card" style="left:-80px">
    <div class="name">Maya Holloway</div><div class="role">Homeowner</div>
    <div class="stars">★★★★★</div><div class="quote">“</div>
    <p>The team arrived on time, fitted every sensor neatly and explained the app step by step. We now feel calm every night at home.</p>
  </div>
  <div class="t-card" style="left:262px">
    <div class="name">Maya Holloway</div><div class="role">Homeowner</div>
    <div class="stars">★★★★★</div><div class="quote">“</div>
    <p>The team arrived on time, fitted every sensor neatly and explained the app step by step. We now feel calm every night at home.</p>
  </div>
  <div class="t-card" style="left:618px">
    <div class="name">Maya Holloway</div><div class="role">Homeowner</div>
    <div class="stars">★★★★★</div><div class="quote">“</div>
    <p>The team arrived on time, fitted every sensor neatly and explained the app step by step. We now feel calm every night at home.</p>
  </div>
  <div class="t-card" style="left:960px">
    <div class="name">Maya Holloway</div><div class="role">Homeowner</div>
    <div class="stars">★★★★★</div><div class="quote">“</div>
    <p>The team arrived on time, fitted every sensor neatly and explained the app step by step. We now feel calm every night at home.</p>
  </div>
</section>

<section class="cta">
  <div class="photo" role="img" aria-label="Colleagues smiling during a meeting in a modern office"></div>
  <div class="inner">
    <div class="eyebrow">Protect your home and business</div>
    <h2>Delivering the Best Security<br>Solutions to Our Clients</h2>
    <a class="btn btn-gold">Get a Free Quote</a>
  </div>
</section>

<section class="news">
  <div class="head">
    <div class="eyebrow">News and Updates</div>
    <h2 class="section-title">Latest News</h2>
  </div>
  <article class="news-main">
    <div class="photo" role="img" aria-label="Modern office building against a blue sky"></div>
    <div class="content">
      <h3>A commercial alarm system that will ensure a swift response</h3>
      <div class="date">Jan 14, 2021</div>
      <p>Fast alerts matter when every second counts. Learn how linked sensors and live monitoring cut response times for stores and offices.</p>
    </div>
  </article>
  <article class="news-item" style="top:116px">
    <div class="thumb" style="background:radial-gradient(circle,#3b6e8f,#1f3347)" role="img" aria-label="Close-up of a dome security camera"></div>
    <div class="meta"><h3>What to do to protect your home before you go on holiday (part 1)</h3><div class="date">Jan 08, 2021</div></div>
  </article>
  <article class="news-item" style="top:276px">
    <div class="thumb" style="background:linear-gradient(135deg,#cfcfcf,#7c7c7c)" role="img" aria-label="Security camera on a building corner"></div>
    <div class="meta"><h3>What to do to protect your home before you go on holiday (part 2)</h3><div class="date">Jan 08, 2021</div></div>
  </article>
  <article class="news-item" style="top:436px">
    <div class="thumb" style="background:linear-gradient(135deg,#b9b3aa,#5b534b)" role="img" aria-label="Hand pressing a home alarm keypad"></div>
    <div class="meta"><h3>What to do to protect your home before you go on holiday (part 3)</h3><div class="date">Jan 08, 2021</div></div>
  </article>
</section>

<footer class="site-footer">
  <div class="logo"><span class="mark"></span>Polar Gate</div>
  <div class="f-col" style="left:180px;top:128px;width:260px">
    <h4>Contact Us</h4>
    <div class="contact-line">
      <svg width="12" height="16" viewBox="0 0 12 16"><path d="M6 0a6 6 0 0 0-6 6c0 4.5 6 10 6 10s6-5.5 6-10a6 6 0 0 0-6-6zm0 8.5A2.5 2.5 0 1 1 6 3.5a2.5 2.5 0 0 1 0 5z" fill="#ccc"/></svg>
      <p>210 Harbour Lane, Suite 4<br>Eastfield, EF 0192</p>
    </div>
    <div class="contact-line">
      <svg width="14" height="14" viewBox="0 0 24 24"><path d="M6.6 10.8a15 15 0 0 0 6.6 6.6l2.2-2.2a1 1 0 0 1 1-.25 11.4 11.4 0 0 0 3.6.6 1 1 0 0 1 1 1V20a1 1 0 0 1-1 1A17 17 0 0 1 3 4a1 1 0 0 1 1-1h3.5a1 1 0 0 1 1 1c0 1.25.2 2.45.6 3.6a1 1 0 0 1-.25 1z" fill="#ccc"/></svg>
      <p>555 0142 730</p>
    </div>
  </div>
  <div class="f-col" style="left:560px;top:60px">
    <h4>Quick Links</h4>
    <ul><li>Home</li><li>About</li><li>Solutions</li><li>Resources</li><li>Contact</li><li>Sitemap</li></ul>
  </div>
  <div class="f-col" style="left:820px;top:60px;width:300px">
    <h4>Sign up for newsletter</h4>
    <p>If you have any questions please<br>send us a message.</p>
    <div class="newsletter"><div class="field">Email address</div><div class="go">Subscribe</div></div>
  </div>
  <div class="f-bottom">
    <div class="socials"><span></span><span></span><span></span><span></span></div>
    <div class="copy">© 2021 Polar Gate. All Rights are Reserved</div>
  </div>
</footer>

</body>
</html>
```